Poster Design for Photography Exhibit

We are looking for a poster design for a photography exhibit featuring high-end fashion and celebrity photography.

Name of the exhibit is "MILES DORVAN: UNTITLED" (please use Helvetica Black all cap for show name.

Poster is LANDSCAPE format (2 units wide by 1 unit high).

Unfortunately due to legal reasons, we cannot use any actual Miles Dorvan photos. No can we use fashions or people on the poster!

We are looking for a high-end, sexy, bold provocative design that captures the excitement and glamour of a fashion photo shoot.

Target Market(s)

Men and Women interested in Fashion Photography and art photography in general

Industry/Entity Type

Fashion

Requirements
Must have
• landscape format, name of exhibit in Helvetica Black all caps
Nice to have
• Can be grayscale or color.
Should not have
• Logos or brand names

```html
<!DOCTYPE html>
<html lang="en">
<head>
<meta charset="UTF-8">
<title>Miles Dorvan: Untitled — Exhibition Poster</title>
<link href="https://fonts.googleapis.com/css2?family=Archivo+Black&display=swap" rel="stylesheet">
<style>
  :root {
    --paper: #eeede8;
    --lens-core: #0b0d0e;
    --lens-mid: #1c2224;
    --lens-rim: #2a2f31;
    --band: rgba(58, 58, 58, 0.76);
    --rule: rgba(255, 255, 255, 0.85);
    --type: #ffffff;
  }
  * { margin: 0; padding: 0; box-sizing: border-box; }
  html, body {
    width: 1200px;
    height: 768px;
    overflow: hidden;
    background: var(--paper);
  }
  .poster {
    position: relative;
    width: 1200px;
    height: 768px;
    overflow: hidden;
    background: var(--paper);
  }
  .lens-photo {
    position: absolute;
    left: -175px;
    top: -60px;
    width: 860px;
    height: 860px;
    border-radius: 50%;
    background:
      radial-gradient(circle at 50% 50%, #2a3b3c 0 4%, var(--lens-core) 9%, #141a1c 20%, #23302f 27%, var(--lens-core) 33%, #1a2021 45%, var(--lens-mid) 70%, var(--lens-rim) 88%, #111 100%);
  }
  .info-band {
    position: absolute;
    left: 210px;
    top: 365px;
    width: 990px;
    height: 403px;
    background: var(--band);
  }
  .divider {
    position: absolute;
    left: 0;
    top: 664px;
    width: 1200px;
    height: 1px;
    background: var(--rule);
  }
  .show-title,
  .artist-name {
    position: absolute;
    right: 26px;
    color: var(--type);
    font-family: "Archivo Black", "Helvetica Neue", Arial, sans-serif;
    text-transform: uppercase;
    line-height: 1;
    white-space: nowrap;
    text-align: right;
  }
  .show-title {
    top: 583px;
    font-size: 84px;
    letter-spacing: 1px;
  }
  .artist-name {
    top: 678px;
    font-size: 60px;
    letter-spacing: 1px;
  }
</style>
</head>
<body>
  <main class="poster">
    <div class="lens-photo" role="img" aria-label="Close-up photograph of a camera lens with teal and magenta reflections"></div>
    <div class="info-band"></div>
    <div class="divider"></div>
    <h1 class="show-title">Untitled</h1>
    <h2 class="artist-name">Miles Dorvan</h2>
  </main>
</body>
</html>
```